Business Card Design

We are a contracting firm, 95% of my work is interior renovations.... but also don't want to preclude the idea of doing exterior work if it arises. I Need a business card that says I am the ultimate professional. There is a per-determined notion that all contractors are shady, unreliable, etc. Being that most of my work is in Manhattan, I would like to give the impression of fresh, modern, sleek, design/build firm.

Target Market(s)

young couples 25-40

Industry/Entity Type

Business

Contact Information for Business Card

PeterHollowayBuilders LLC
27 North Birchwood Lane
Elm Hollow NY 11000
718-555-0193
646-555-0148- cell
www.phbrx.com
ph@phbrx.com
Peter Holloway

Requirements
Should not have
• do not want to give the impression of a "bargain basement store"

```html
<!DOCTYPE html>
<html lang="en">
<head>
<meta charset="utf-8">
<title>PeterHollowayBuilders – Business Card</title>
<link href="https://fonts.googleapis.com/css2?family=Open+Sans:wght@400;600;700&display=swap" rel="stylesheet">
<style>
  :root {
    --backdrop: #d8d3cc;
    --card-dark: #1c1c1c;
    --card-mid: #2a2a2a;
    --panel: rgba(70, 70, 70, 0.85);
    --text-main: #ffffff;
    --text-soft: #e6e6e6;
    --text-muted: #cfcfcf;
  }
  * { margin: 0; padding: 0; box-sizing: border-box; }
  html, body {
    width: 1200px;
    height: 1043px;
    overflow: hidden;
    background: var(--backdrop);
    font-family: "Open Sans", Arial, sans-serif;
  }
  .canvas { position: relative; width: 1200px; height: 1043px; }
  .card {
    position: absolute;
    width: 808px;
    height: 462px;
    overflow: hidden;
    color: var(--text-main);
    box-shadow: 0 6px 18px rgba(0,0,0,0.25);
  }
  .card__surface {
    position: absolute; inset: 0;
    background: radial-gradient(ellipse at 50% 40%, var(--card-mid) 0%, var(--card-dark) 75%);
  }
  .card--front { left: 37px; top: 47px; }
  .card--back  { left: 356px; top: 548px; }

  .brand-panel {
    position: absolute;
    left: 0; top: 156px;
    width: 489px; height: 149px;
    background: var(--panel);
    border-radius: 0 40px 40px 0;
  }
  .brand-panel__name {
    position: absolute;
    left: 0; width: 489px; top: 44px;
    text-align: center;
    font-size: 33px;
    font-weight: 600;
    color: var(--text-main);
    letter-spacing: -0.3px;
  }
  .brand-panel__tagline {
    position: absolute;
    left: 0; width: 489px; top: 96px;
    text-align: center;
    font-size: 16px;
    font-weight: 400;
    color: var(--text-muted);
  }

  .contact {
    position: absolute;
    right: 25px; top: 215px;
    text-align: right;
  }
  .contact__person { font-size: 26px; font-weight: 700; margin-bottom: 42px; }
  .contact__list { list-style: none; }
  .contact__item {
    display: flex; justify-content: flex-end; align-items: center;
    gap: 8px;
    font-size: 21px; line-height: 37px;
    color: var(--text-soft);
  }
  .contact__icon { width: 18px; height: 18px; fill: var(--text-soft); }

  .company {
    position: absolute; left: 0; width: 100%;
    text-align: center;
  }
  .company__name { top: 210px; font-size: 24px; font-weight: 600; }
  .company__address { top: 250px; font-size: 21px; color: var(--text-soft); }
  .company__web { top: 378px; font-size: 27px; letter-spacing: 4px; color: var(--text-soft); }
</style>
</head>
<body>
<div class="canvas">

  <section class="card card--front">
    <div class="card__surface" role="img" aria-label="Dark charcoal linen texture background"></div>
    <div class="brand-panel">
      <div class="brand-panel__name">PeterHollowayBuilders</div>
      <div class="brand-panel__tagline">General Contracting &amp; Construction Services</div>
    </div>
    <div class="contact">
      <div class="contact__person">Peter Holloway</div>
      <ul class="contact__list">
        <li class="contact__item">
          <svg class="contact__icon" viewBox="0 0 24 24"><path d="M6.6 10.8a15 15 0 0 0 6.6 6.6l2.2-2.2a1 1 0 0 1 1-.25 11.4 11.4 0 0 0 3.6.57 1 1 0 0 1 1 1V20a1 1 0 0 1-1 1A17 17 0 0 1 3 4a1 1 0 0 1 1-1h3.5a1 1 0 0 1 1 1c0 1.25.2 2.45.57 3.6a1 1 0 0 1-.25 1z"/></svg>
          718-555-0193
        </li>
        <li class="contact__item">
          <svg class="contact__icon" viewBox="0 0 24 24"><path d="M7 1h10a2 2 0 0 1 2 2v18a2 2 0 0 1-2 2H7a2 2 0 0 1-2-2V3a2 2 0 0 1 2-2zm0 3v13h10V4zm5 15a1.3 1.3 0 1 0 0 2.6 1.3 1.3 0 0 0 0-2.6z"/></svg>
          646-555-0148
        </li>
        <li class="contact__item">
          <svg class="contact__icon" viewBox="0 0 24 24"><path d="M2 9l10-6 10 6v11H2zm2.4 1L12 14.6 19.6 10 12 5.4z"/></svg>
          ph@phbrx.com
        </li>
        <li class="contact__item">
          <svg class="contact__icon" viewBox="0 0 24 24"><path d="M12 2a10 10 0 1 0 0 20 10 10 0 0 0 0-20zm6.9 6h-3a15 15 0 0 0-1.4-3.9A8 8 0 0 1 18.9 8zM12 4a13 13 0 0 1 1.9 4h-3.8A13 13 0 0 1 12 4zM4.3 14a8 8 0 0 1 0-4h3.4a16 16 0 0 0 0 4zm.8 2h3a15 15 0 0 0 1.4 3.9A8 8 0 0 1 5.1 16zM8 8H5.1a8 8 0 0 1 4.4-3.9A15 15 0 0 0 8 8zm4 12a13 13 0 0 1-1.9-4h3.8A13 13 0 0 1 12 20zm2.3-6H9.7a14 14 0 0 1 0-4h4.6a14 14 0 0 1 0 4zm.2 5.9a15 15 0 0 0 1.4-3.9h3a8 8 0 0 1-4.4 3.9zm1.8-5.9a16 16 0 0 0 0-4h3.4a8 8 0 0 1 0 4z"/></svg>
          www.phbrx.com
        </li>
      </ul>
    </div>
  </section>

  <section class="card card--back">
    <div class="card__surface" role="img" aria-label="Dark charcoal linen texture background"></div>
    <div class="company company__name">PeterHollowayBuilders LLC</div>
    <div class="company company__address">27 North Birchwood Lane Elm Hollow NY 11000</div>
    <div class="company company__web">www.phbrx.com</div>
  </section>

</div>
</body>
</html>
```